Website for company called VORENTbio

We need a website for our new company called VORENTbio which developed a platform/technology to identify antigen-specific T cells (immune cells) which can be used for cancer therapy, autoimmunity, etc.

The platform is called VORENT and is rapid, versatile, unbiased, and inexpensive.

We have a semi-final logo although we are not completely set on color and font of text (attached).

Target Market(s)

Our target audience at the moment would be potential investors and VCs. We eventually are interested in getting attention from scientists and cell/immunotherapy companies.

Industry/Entity Type

Healthcare/Technology

Coding

Coded - Design and coding required

Number of Pages Required

1 page

Colors
0094D4
00A9DD
6FCCEA
C7EBF8
E9F6FB
00AB8E
00BBA5
67D7C9
C6EFE9
E9F9F6
E54698
E96AAD
F1A4CE
F9D9EA
FCEFF6
A7469A
B969AE
D3A5CF
EDDBEB
F8F0F9
6B429C
8869AF
B7A5CE
E3DAEB
F3F0F8

Requirements
Must have
• Landing page about the company, About us page, Technology page (could be merged with company landing page), Contact us page

```html
<!DOCTYPE html>
<html lang="en">
<head>
<meta charset="utf-8">
<title>VORENTbio – T Cell Discovery for Precision Immunotherapy</title>
<link href="https://fonts.googleapis.com/css2?family=Poppins:ital,wght@0,300;0,400;0,500;0,600;1,400&display=swap" rel="stylesheet">
<style>
:root{
  --teal:#00ab8e;
  --blue:#1d5ba8;
  --blue-band:#1b5eac;
  --ink:#222222;
  --text:#555a60;
  --muted:#7a7f86;
  --light:#f0f1f3;
  --footer:#232323;
  --white:#ffffff;
}
*{margin:0;padding:0;box-sizing:border-box}
html,body{width:1200px;height:4644px;overflow:hidden}
body{font-family:"Poppins",sans-serif;color:var(--ink);background:var(--white);position:relative}
.abs{position:absolute}
.shape{position:absolute}

/* top bar */
.topbar{position:absolute;left:0;top:0;width:1200px;height:38px;background:var(--teal)}
.topbar .social{position:absolute;top:12px;display:flex;gap:22px;left:160px}
.dot{width:13px;height:13px;border-radius:50%;background:rgba(255,255,255,.9);display:block}
.topbar .contact{position:absolute;top:0;right:160px;height:38px;display:flex;align-items:center;gap:34px;color:#fff;font-size:12px}
.topbar .contact span{display:flex;align-items:center;gap:8px}

/* hero */
.hero{position:absolute;left:0;top:38px;width:1200px;height:659px;
  background:radial-gradient(ellipse 520px 420px at 900px 220px,#b0123a 0%,#6a1a6a 35%,rgba(40,20,80,0) 70%),
  radial-gradient(ellipse 500px 500px at 1050px 520px,#3a2c8a 0%,rgba(20,20,60,0) 70%),
  linear-gradient(90deg,#05050a 0%,#0c0b1a 45%,#1a1236 100%)}
.brand{position:absolute;display:flex;align-items:center;gap:10px;font-weight:500;color:#fff}
.brand .mark{border-radius:50%;background:currentColor;display:block}
.hero .brand{left:162px;top:70px;font-size:24px}
.hero .brand .mark{width:16px;height:16px}
.nav{position:absolute;top:82px;left:0;width:1200px;height:20px}
.nav a{position:absolute;color:#fff;font-size:12px;text-decoration:none;letter-spacing:.2px}
.hero h1{position:absolute;left:158px;top:225px;width:560px;font-weight:400;font-size:47px;line-height:53px;color:#fff}
.hero h1 b{font-weight:600}
.hero p{position:absolute;left:162px;top:404px;width:510px;font-size:13px;line-height:18px;color:#fff}
.btn{position:absolute;background:var(--blue);color:#fff;font-size:12px;font-weight:500;display:flex;align-items:center;justify-content:center}
.hero .btn{left:162px;top:465px;width:136px;height:36px}

/* about */
.about h2{position:absolute;left:160px;top:862px;font-size:30px;font-weight:400}
.about p{position:absolute;left:160px;width:370px;font-size:12.5px;line-height:19px;color:var(--text)}
.photo{position:absolute}

/* care box */
.care{position:absolute;left:160px;top:1348px;width:878px;height:144px;background:var(--light);border-radius:6px 6px 0 0}
.care .mark{position:absolute;left:48px;top:44px;width:56px;height:56px;border-radius:50%;background:var(--teal)}
.care .msg{position:absolute;left:240px;top:50px;width:380px;text-align:center;font-size:15px;line-height:20px;color:#333}
.care .msg b{font-weight:600;font-size:15px}
.care .call{position:absolute;right:40px;top:60px;color:var(--blue);font-weight:600;font-size:16px}
.pillar{position:absolute;top:1492px;height:189px;color:#fff;padding:52px 38px 0}
.pillar h3{font-size:19px;font-weight:500;margin-bottom:14px}
.pillar p{font-size:12.5px;line-height:19px}
.vision{left:160px;width:438px;background:var(--teal);border-radius:0 0 0 6px}
.mission{left:598px;width:440px;background:var(--blue);border-radius:0 0 6px 0}

/* harness */
.harness{position:absolute;left:0;top:1757px;width:598px;height:341px;background:var(--blue);color:#fff;padding:32px 52px 0 162px}
.harness h3{font-size:19px;font-weight:500;line-height:23px;margin-bottom:16px}
.harness p{font-size:11.5px;line-height:14.5px;text-align:justify;margin-bottom:10px}

/* headings */
.sec-title{position:absolute;left:0;width:1200px;text-align:center;font-size:30px;font-weight:400}
.sec-sub{position:absolute;left:0;width:1200px;text-align:center;font-size:12px;line-height:19px;color:var(--muted)}

.card-title{position:absolute;font-size:17px;font-weight:500}
.card-text{position:absolute;font-size:12.5px;line-height:19px;color:var(--muted)}

/* testimonial */
.testimonial{position:absolute;left:0;top:3236px;width:1200px;height:345px;background:var(--blue-band);color:#fff}
.testimonial blockquote{position:absolute;left:290px;top:104px;width:740px;font-style:italic;font-size:21.5px;line-height:25px;white-space:nowrap}
.testimonial .who{position:absolute;left:288px;top:228px;font-weight:600;font-size:15px;display:flex;align-items:center;gap:22px}
.testimonial .role{position:absolute;left:288px;top:254px;font-size:14px}

/* news */
.news-title{position:absolute;font-size:15px;font-weight:500;line-height:18px;width:270px}
.news-meta{position:absolute;font-size:11px;line-height:16px;color:var(--muted)}
.news-meta em{font-style:normal;color:var(--blue);display:block}

.big-brand{position:absolute;left:0;top:4262px;width:1200px;display:flex;justify-content:center;align-items:center;gap:20px;color:var(--ink);font-size:62px;font-weight:500}
.big-brand .mark{width:60px;height:60px;border-radius:50%;background:var(--teal)}

/* footer */
.footer{position:absolute;left:0;top:4424px;width:1200px;height:220px;background:var(--footer);color:#fff}
.footer .fnav a{position:absolute;top:42px;font-size:11.5px;color:#fff;text-decoration:none}
.footer .rule{position:absolute;left:160px;top:92px;width:880px;height:1px;background:#3a3a3a}
.footer .rule.b{top:160px}
.footer .info{position:absolute;top:110px;display:flex;align-items:center;gap:12px;font-size:13px}
.footer .info i{width:26px;height:26px;border-radius:50%;background:var(--teal);display:flex;align-items:center;justify-content:center}
.footer .social{position:absolute;top:180px;left:550px;display:flex;gap:20px}
</style>
</head>
<body>

<header class="topbar">
  <div class="social"><span class="dot"></span><span class="dot"></span><span class="dot"></span></div>
  <div class="contact">
    <span><svg width="12" height="12" viewBox="0 0 24 24"><path fill="#fff" d="M6.6 10.8a15 15 0 006.6 6.6l2.2-2.2a1 1 0 011-.24 11.4 11.4 0 003.6.57 1 1 0 011 1V20a1 1 0 01-1 1A17 17 0 013 4a1 1 0 011-1h3.5a1 1 0 011 1 11.4 11.4 0 00.57 3.6 1 1 0 01-.25 1z"/></svg>555-302-0147</span>
    <span><svg width="13" height="10" viewBox="0 0 26 20"><rect x="1" y="1" width="24" height="18" fill="#fff"/><path d="M1 1l12 10L25 1" stroke="#00ab8e" stroke-width="2" fill="none"/></svg>hello@vorentbio-mail.com</span>
  </div>
</header>

<section class="hero">
  <div class="shape" role="img" aria-label="Close-up of a glowing DNA double helix and cells in red and violet light" style="left:560px;top:0;width:640px;height:659px;background:radial-gradient(ellipse 300px 260px at 330px 200px,rgba(220,30,70,.55),rgba(0,0,0,0) 70%)"></div>
  <div class="brand"><span class="mark"></span>VORENTbio</div>
  <nav class="nav">
    <a style="left:420px">HOME</a><a style="left:505px">ABOUT</a><a style="left:598px">TECHNOLOGY</a><a style="left:732px">TESTIMONIALS</a><a style="left:874px">NEWS</a><a style="left:958px">CONTACT US</a>
  </nav>
  <h1>Revolutionizing <b>T Cell Discovery</b> for Precision Immunotherapy</h1>
  <p>VORENTbio's proprietary VORENT platform enables the rapid, unbiased identification of antigen-specific T cells.</p>
  <a class="btn">Learn More</a>
</section>

<section class="about">
  <h2>About Us</h2>
  <p style="top:910px">At Meridale Care Infusion a commitment to quality is our priority.</p>
  <p style="top:968px;width:330px">The leaders at Meridale Care Infusion have teamed together to reshape the future of home infusion with excellence, innovation, and clinical expertise.</p>
  <p style="top:1065px">Our professional staff and innovative service programs make Meridale Care Infusion the obvious choice as your partner for infusion therapy.</p>
  <a class="btn" style="left:160px;top:1146px;width:138px;height:36px">Contact Us</a>
  <div class="photo" role="img" aria-label="Gloved hand pipetting blue liquid into a rack of test tubes" style="left:634px;top:777px;width:404px;height:403px;background:linear-gradient(160deg,#e9f3f7 0%,#9fd3e6 40%,#1a9bc6 75%,#0f6f9a 100%)"></div>
  <div class="photo" role="img" aria-label="Scientist in protective suit working in a clean lab" style="left:582px;top:1101px;width:216px;height:173px;background:linear-gradient(150deg,#f2f4f3 0%,#c9d2cf 60%,#9aa6a3 100%)"></div>
</section>

<section>
  <div class="care">
    <span class="mark"></span>
    <div class="msg"><b>We are here for you!</b><br>Our care can make a difference in your healing!</div>
    <div class="call">Call: 555-302-0147</div>
  </div>
  <div class="pillar vision"><h3>Our Vision</h3><p>The VORENT™ platform enables the direct detection and profiling of antigen-specific T cells from patient restriction.</p></div>
  <div class="pillar mission"><h3>Our Mission</h3><p>The VORENT™ platform enables the direct detection and profiling of antigen-specific T cells from patient restriction.</p></div>
</section>

<section>
  <div class="harness">
    <h3>Harnessing The Power of The<br>Immune System</h3>
    <p>We make the referral process as easy as possible for case managers and physicians. Please fax or email order, demographics, allergies, height, weight, access, and discharge information. We will then have financial approval within the hour, and usually can deliver medications within 24 hours of the receipt of the order.</p>
    <p>If it is indicated that the patient needs home health, we will then locate a home health that is in network for the patient and coordinate all care needed.</p>
    <p>Please call our intake specialist if you have any questions. We look forward to serving your patients and thank you for trusting us to care for them.</p>
  </div>
  <div class="photo" role="img" aria-label="Researcher at a laptop beside a microscope and rack of blue sample tubes" style="left:598px;top:1757px;width:602px;height:341px;background:linear-gradient(120deg,#cfd5da 0%,#eef1f3 45%,#9fd6e2 75%,#5b8ea0 100%)"></div>
</section>

<section>
  <h2 class="sec-title" style="top:2162px">Our Technology</h2>
  <p class="sec-sub" style="top:2215px">You can be assured – we have a commitment to excellence when it comes to the<br>level of care we provide to each and every patient.</p>

  <div class="photo" role="img" aria-label="Lab bench with blue and orange solutions in glassware and a microscope" style="left:160px;top:2280px;width:579px;height:239px;background:linear-gradient(90deg,#2c6fc0 0%,#8fb2dd 35%,#eef0f2 60%,#b8bcc0 100%)"></div>
  <div class="photo" role="img" aria-label="Blue illustration of a neuron-like immune cell" style="left:762px;top:2280px;width:276px;height:239px;background:radial-gradient(circle at 60% 55%,#4fb6e6 0%,#1a78b8 45%,#0a3f6e 100%)"></div>
  <div class="card-title" style="left:160px;top:2542px">Antigen-Agnostic</div>
  <div class="card-text" style="left:160px;top:2582px;width:580px">This IV infusion of antibiotic, antiviral, or antifungal drugs, is used to treat infections<br>that do not respond to oral medications. Infectious diseases occur when the immune<br>system fails to kill pathogenic microorganisms that grow within the body and cause<br>disease.</div>
  <div class="card-title" style="left:762px;top:2542px">High-Throughput</div>
  <div class="card-text" style="left:762px;top:2582px;width:280px">When orders are received by the<br>physician to provide home inotrope<br>therapy, MCI will provide the medication,<br>pump and supplies...</div>

  <div class="photo" role="img" aria-label="Gloved hands holding a sample tube" style="left:160px;top:2703px;width:276px;height:241px;background:linear-gradient(140deg,#eaf0f4 0%,#6fb6e2 55%,#1d6fb0 100%)"></div>
  <div class="photo" role="img" aria-label="Scientist pipetting samples into a rack in a busy lab" style="left:460px;top:2703px;width:578px;height:241px;background:linear-gradient(110deg,#9ec9e4 0%,#dfe8ee 45%,#6f8fa8 80%,#c44a5a 100%)"></div>
  <div class="card-title" style="left:160px;top:2966px">Low Sample Input</div>
  <div class="card-text" style="left:160px;top:3006px;width:280px">Specialty injectables are used for the<br>treatment of chronic and/or<br>life-threatening diseases. Due to their<br>complex nature...</div>
  <div class="card-title" style="left:460px;top:2966px">Scalable &amp; Affordable</div>
  <div class="card-text" style="left:460px;top:3006px;width:590px">Parenteral (intravenous) nutrition (PN), often called total parenteral nutrition (TPN), is<br>the medical term for infusing a specialized form of food through a vein. Its goal is to<br>treat or prevent malnutrition. It is typically used for people whose digestive systems<br>either can't absorb or can't tolerate adequate food eaten by mouth.</div>

  <a class="btn" style="left:508px;top:3123px;width:182px;height:38px">View All Technology</a>
</section>

<section class="testimonial">
  <svg class="abs" style="left:30px;top:160px" width="20" height="24" viewBox="0 0 20 24"><path d="M14 2L4 12l10 10" stroke="#fff" stroke-width="2" fill="none"/></svg>
  <svg class="abs" style="left:1146px;top:160px" width="20" height="24" viewBox="0 0 20 24"><path d="M6 2l10 10L6 22" stroke="#fff" stroke-width="2" fill="none"/></svg>
  <svg class="abs" style="left:222px;top:120px" width="46" height="46" viewBox="0 0 46 46"><circle cx="23" cy="23" r="21" fill="none" stroke="#fff" stroke-width="2.5"/><path d="M13 28v-5c0-4 2-7 6-8l1 2c-2 1-3 2-3 4h3v7zM25 28v-5c0-4 2-7 6-8l1 2c-2 1-3 2-3 4h3v7z" fill="#fff"/></svg>
  <blockquote>“I should be incapable of drawing a single stroke at the present<br>moment; and yet I feel that I never was a greater artist than now.<br>The lovely valley teems with vapor around me, &amp; the<br>meridian sun strikes.</blockquote>
  <div class="who">Marcus Ellery
    <svg width="98" height="18" viewBox="0 0 98 18"><g fill="#fff"><path id="s" d="M9 0l2.6 6 6.4.5-4.9 4.2 1.5 6.3L9 13.6 3.4 17l1.5-6.3L0 6.5 6.4 6z"/><use href="#s" x="20"/><use href="#s" x="40"/><use href="#s" x="60"/><use href="#s" x="80"/></g></svg>
  </div>
  <div class="role">CEO</div>
</section>

<section>
  <h2 class="sec-title" style="top:3644px">Our News</h2>
  <p class="sec-sub" style="top:3697px">You can be assured – we have a commitment to excellence when it comes to the<br>level of care we provide to each and every patient.</p>

  <div class="photo" role="img" aria-label="Two researchers in masks examining a flask of blue liquid" style="left:160px;top:3761px;width:276px;height:205px;background:linear-gradient(150deg,#dfe9ef 0%,#7fbbd9 50%,#2a79a8 100%)"></div>
  <div class="photo" role="img" aria-label="Illustration of a DNA helix among blue cells" style="left:461px;top:3761px;width:276px;height:205px;background:radial-gradient(circle at 50% 55%,#c94a4a 0%,#3d7ec4 35%,#123f78 100%)"></div>
  <div class="photo" role="img" aria-label="Scientist in goggles pipetting a red sample" style="left:762px;top:3761px;width:276px;height:205px;background:linear-gradient(150deg,#e9eef1 0%,#82c3de 55%,#2d87b4 100%)"></div>

  <div class="news-title" style="left:160px;top:3986px">7 Tips to Improve your Mental<br>Health in 2024</div>
  <div class="news-title" style="left:461px;top:3986px">PTSD: Causes, Symptoms, &amp; When<br>to Seek Treatment</div>
  <div class="news-title" style="left:762px;top:3986px">Is counselling free in<br>Manitoba?</div>

  <div class="card-text" style="left:160px;top:4032px;width:276px;font-size:11.5px;line-height:18px">Consectetuer fringilla aenean sagittis potenti ullamcorper nam porta feugiat</div>
  <div class="card-text" style="left:461px;top:4032px;width:276px;font-size:11.5px;line-height:18px">Consectetuer fringilla aenean sagittis potenti ullamcorper nam porta feugiat</div>
  <div class="card-text" style="left:762px;top:4032px;width:276px;font-size:11.5px;line-height:18px">Consectetuer fringilla aenean sagittis potenti ullamcorper nam porta feugiat</div>

  <div class="news-meta" style="left:162px;top:4094px"><em>Virtual Assistant</em>Jan 02, 2025</div>
  <div class="news-meta" style="left:463px;top:4094px"><em>Virtual Assistant</em>Jan 02, 2025</div>
  <div class="news-meta" style="left:764px;top:4094px"><em>Virtual Assistant</em>Jan 02, 2025</div>

  <a class="btn" style="left:528px;top:4166px;width:144px;height:36px">View All News</a>
</section>

<div class="big-brand"><span class="mark"></span>VORENTbio</div>

<footer class="footer">
  <nav class="fnav">
    <a style="left:275px">HOME</a><a style="left:371px">ABOUT</a><a style="left:473px">TECHNOLOGY</a><a style="left:612px">TESTIMONIALS</a><a style="left:758px">NEWS</a><a style="left:852px">CONTACT US</a>
  </nav>
  <div class="rule"></div>
  <div class="info" style="left:246px"><i><svg width="12" height="12" viewBox="0 0 24 24"><path fill="#fff" d="M6.6 10.8a15 15 0 006.6 6.6l2.2-2.2a1 1 0 011-.24 11.4 11.4 0 003.6.57 1 1 0 011 1V20a1 1 0 01-1 1A17 17 0 013 4a1 1 0 011-1h3.5a1 1 0 011 1 11.4 11.4 0 00.57 3.6 1 1 0 01-.25 1z"/></svg></i>555-302-0147</div>
  <div class="info" style="left:480px"><i><svg width="12" height="9" viewBox="0 0 26 20"><rect x="1" y="1" width="24" height="18" fill="#fff"/><path d="M1 1l12 10L25 1" stroke="#00ab8e" stroke-width="2" fill="none"/></svg></i>hello@vorentbio-mail.com</div>
  <div class="info" style="left:764px"><i><svg width="10" height="13" viewBox="0 0 20 26"><path fill="#fff" d="M10 0a9 9 0 00-9 9c0 7 9 17 9 17s9-10 9-17a9 9 0 00-9-9zm0 12a3 3 0 110-6 3 3 0 010 6z"/></svg></i>122, Lorem ipsum dolird</div>
  <div class="rule b"></div>
  <div class="social"><span class="dot"></span><span class="dot"></span><span class="dot"></span></div>
</footer>

</body>
</html>
```